One Page Sales Flyer for Wireless Survey- Computer Hardware

I want a designer to create a one page 4 color sales slick to be given to our sales team to sell to the end customers. I would like a visual picture of a heat map so zavvix "heat map wireless" to get an idea of how that image should look.

```html
<!DOCTYPE html>
<html lang="en">
<head>
<meta charset="utf-8">
<title>Wireless Site Surveys – Sales Sheet</title>
<link rel="stylesheet" href="https://fonts.googleapis.com/css2?family=Raleway:wght@300;400;600;700&family=Montserrat:wght@400;500&display=swap">
<style>
  :root {
    --navy: #1b2d5e;
    --navy-deep: #13295a;
    --lime: #7dff00;
    --lime-text: #6ee000;
    --charcoal: #1c2021;
    --sky: #4cc3f4;
    --white: #ffffff;
    --ink: #222222;
  }
  * { margin: 0; padding: 0; box-sizing: border-box; }
  html, body { width: 848px; height: 1200px; overflow: hidden; background: var(--white); }
  body { font-family: "Raleway", Arial, sans-serif; color: var(--ink); position: relative; }

  .hero { position: absolute; left: 0; top: 0; width: 848px; height: 312px; }
  .hero-art {
    position: absolute; inset: 0;
    background: linear-gradient(105deg, #d9b98a 0%, #8aa6a0 30%, #2f6fb8 62%, #1452b8 100%);
  }
  .hero-brand {
    position: absolute; top: 84px; left: 0; width: 848px; text-align: center;
    font: 600 20px/1 "Raleway", Arial, sans-serif; color: #2a63c8; letter-spacing: 1px;
  }
  .hero-band {
    position: absolute; left: 0; top: 190px; width: 848px; height: 122px;
    background: linear-gradient(90deg, rgba(30,40,52,.92), rgba(22,48,100,.92));
    padding: 33px 0 0 51px;
  }
  .hero-title { font-weight: 300; font-size: 32px; line-height: 29px; letter-spacing: .2px; }
  .hero-title .line-1 { color: var(--white); display: block; }
  .hero-title .line-2 { color: var(--lime); display: block; }

  .intro { position: absolute; left: 0; top: 312px; width: 848px; height: 204px; }
  .heatmap {
    position: absolute; left: 78px; top: 24px; width: 142px; height: 142px; border-radius: 10px;
    background: linear-gradient(160deg, #f0263a 0%, #f2552a 35%, #f59a22 60%, #e6d028 80%, #a8e05a 100%);
  }
  .intro-text {
    position: absolute; left: 261px; top: 22px; width: 540px;
    font-size: 16.4px; line-height: 28.6px; color: var(--navy-deep);
  }
  .intro-text strong { color: var(--lime-text); font-weight: 600; }

  .targets { position: absolute; left: 0; top: 516px; width: 848px; height: 320px; }
  .targets svg { position: absolute; left: 0; top: 0; }
  .why-need {
    position: absolute; left: 548px; top: 0; width: 300px; height: 320px;
    background: var(--lime); padding: 24px 18px 0 18px; color: var(--white);
  }
  .why-need h2 { font-weight: 300; font-size: 31px; line-height: 29px; letter-spacing: .3px; }
  .why-need .rule { width: 38px; height: 3px; background: var(--white); margin: 14px 0 18px; }
  .why-need p { font-family: "Montserrat", Arial, sans-serif; font-size: 10.2px; line-height: 17.6px; width: 240px; }

  .reasons { position: absolute; left: 0; top: 836px; width: 848px; height: 318px; }
  .reasons h2 {
    position: absolute; top: 20px; width: 848px; text-align: center;
    font-weight: 400; font-size: 32.5px; color: var(--navy); letter-spacing: .2px;
  }
  .reason-icon { position: absolute; }
  .reason-text {
    position: absolute; top: 161px; width: 200px; text-align: center;
    font-family: "Montserrat", Arial, sans-serif; font-size: 10.6px; line-height: 17.6px; color: var(--ink);
  }
  .reason-divider { position: absolute; top: 160px; width: 1px; height: 20px; background: #bbbbbb; }

  .footer {
    position: absolute; left: 0; top: 1154px; width: 848px; height: 46px; background: var(--sky);
    display: flex; align-items: center; justify-content: center;
    font: 600 15px/1 "Raleway", Arial, sans-serif; color: var(--white); letter-spacing: 1px;
  }
</style>
</head>
<body>

<header class="hero">
  <div class="hero-art" role="img" aria-label="Abstract network of white nodes and connecting lines over a warm-to-blue gradient"></div>
  <div class="hero-brand">Quorvane</div>
  <div class="hero-band">
    <h1 class="hero-title">
      <span class="line-1">INCREASE HARDWARE AND SERVICES SPEND</span>
      <span class="line-2">WITH WIRELESS SITE SURVEYS</span>
    </h1>
  </div>
</header>

<section class="intro">
  <div class="heatmap" role="img" aria-label="Wireless signal heat map over a floor plan, red to yellow-green"></div>
  <p class="intro-text">A <strong>Wireless Site Survey</strong> is a compilation of reports showing a visual representation of health of your wireless network. This does not only show how strong or weak a wireless signal is in any location it also helps aid in channel and placement to ensure maximum stable data rates are archived even where the single appears strong.</p>
</section>

<section class="targets">
  <svg width="548" height="320" viewBox="0 0 548 320" aria-label="Target customers">
    <rect width="548" height="320" fill="#1c2021"/>
    <g stroke="#7dff00" stroke-width="1.4" fill="none">
      <line x1="154" y1="63" x2="256" y2="63"/>
      <line x1="304" y1="54" x2="398" y2="54"/>
      <line x1="376" y1="92" x2="526" y2="92"/>
      <line x1="101" y1="115" x2="210" y2="115"/>
      <line x1="400" y1="153" x2="530" y2="153"/>
      <line x1="44" y1="182" x2="204" y2="182"/>
      <line x1="392" y1="214" x2="486" y2="214"/>
      <line x1="154" y1="238" x2="242" y2="238"/>
      <line x1="333" y1="256" x2="440" y2="256"/>
      <line x1="174" y1="280" x2="290" y2="280"/>
      <line x1="290" y1="262" x2="290" y2="280"/>
    </g>
    <circle cx="304" cy="158" r="100" fill="none" stroke="#7dff00" stroke-width="6" stroke-dasharray="40 10"/>
    <circle cx="304" cy="158" r="88" fill="#1b2d5e"/>
    <g font-family="Raleway, Arial, sans-serif" font-weight="300" font-size="16" fill="#ffffff">
      <text x="164" y="60">Distributors</text>
      <text x="333" y="51">SLED</text>
      <text x="390" y="89">Enterprise F1000</text>
      <text x="110" y="112">Warehouses</text>
      <text x="413" y="150">Sports Venues</text>
      <text x="57" y="179">Medical/Hospitals</text>
      <text x="406" y="211">Stadiums</text>
      <text x="177" y="235">K-12</text>
      <text x="378" y="253">Hotels</text>
      <text x="185" y="277">Retail Stores</text>
    </g>
    <g font-family="Raleway, Arial, sans-serif" font-weight="700" font-size="23" text-anchor="middle">
      <text x="304" y="153" fill="#7dff00">TARGET</text>
      <text x="304" y="178" fill="#ffffff">CUSTOMERS</text>
    </g>
  </svg>
  <div class="why-need">
    <h2>WHY DO<br>CUSTOMERS<br>NEED A<br>SITE SURVEY?</h2>
    <div class="rule"></div>
    <p>Any variety of factors can contribute to an unhealthy wireless network (electrical, motors, materials used in construction, distance, neighboring wireless networks, etc.) and traditional methods that use only blueprints and a computer program to show signal strength have shown to be ineffective.</p>
  </div>
</section>

<section class="reasons">
  <h2>WHY SHOULD THEY USE YOU?</h2>

  <svg class="reason-icon" style="left:98px; top:92px" width="70" height="50" viewBox="0 0 72 52" aria-hidden="true">
    <path d="M4 18 A46 46 0 0 1 68 18" stroke="#bfe6f8" stroke-width="5" fill="none" stroke-linecap="round"/>
    <path d="M14 29 A31 31 0 0 1 58 29" stroke="#1b2d5e" stroke-width="6" fill="none" stroke-linecap="round"/>
    <path d="M24 40 L36 50 L48 40 A17 17 0 0 0 24 40 Z" fill="#6fe000"/>
  </svg>
  <p class="reason-text" style="left:33px">42% of businesses report some<br>issues with wireless connectivity<br>and acknowledge its effect<br>on the bottom line*</p>
  <div class="reason-divider" style="left:230px"></div>

  <svg class="reason-icon" style="left:282px; top:84px" width="70" height="70" viewBox="0 0 70 70" aria-hidden="true">
    <g fill="#6fe000">
      <circle cx="35" cy="35" r="27"/>
      <g transform="translate(35 35)">
        <rect x="-6" y="-35" width="12" height="12"/><rect x="-6" y="23" width="12" height="12"/>
        <rect x="-35" y="-6" width="12" height="12"/><rect x="23" y="-6" width="12" height="12"/>
        <g transform="rotate(45)"><rect x="-6" y="-35" width="12" height="12"/><rect x="-6" y="23" width="12" height="12"/>
        <rect x="-35" y="-6" width="12" height="12"/><rect x="23" y="-6" width="12" height="12"/></g>
      </g>
    </g>
    <circle cx="35" cy="35" r="18" fill="#ffffff"/>
    <circle cx="35" cy="30" r="6.5" fill="#1b2d5e"/>
    <path d="M23 48 A12 12 0 0 1 47 48 Z" fill="#1b2d5e"/>
  </svg>
  <p class="reason-text" style="left:217px">Most of these problems are<br>solved through either fine<br>tuning the current equipment<br>(managed services)<br>or purchasing new equipment<br>(incremental sales) of which<br>you can provide both</p>
  <div class="reason-divider" style="left:406px"></div>

  <svg class="reason-icon" style="left:465px; top:92px" width="70" height="50" viewBox="0 0 72 52" aria-hidden="true">
    <g stroke="#6fe000" stroke-width="2.5" fill="none" stroke-linecap="round">
      <path d="M2 6 l4 4 l7 -8"/><path d="M2 19 l4 4 l7 -8"/><path d="M2 32 l4 4 l7 -8"/><path d="M2 45 l4 4 l7 -8"/>
    </g>
    <g stroke="#1b2d5e" stroke-width="3.5">
      <line x1="20" y1="6" x2="68" y2="6"/><line x1="20" y1="19" x2="62" y2="19"/>
      <line x1="20" y1="32" x2="62" y2="32"/><line x1="20" y1="45" x2="68" y2="45"/>
    </g>
  </svg>
  <p class="reason-text" style="left:401px">Being a one-stop shop for all<br>your customer’s IT needs<br>prevents them from needing<br>additional vendors</p>
  <div class="reason-divider" style="left:590px"></div>

  <svg class="reason-icon" style="left:667px; top:90px" width="62" height="54" viewBox="0 0 64 56" aria-hidden="true">
    <polygon points="18,4 46,4 60,28 46,52 18,52 4,28" fill="none" stroke="#6fe000" stroke-width="2.5"/>
    <g fill="#ffffff" stroke="#6fe000" stroke-width="2.5">
      <circle cx="18" cy="4" r="3"/><circle cx="46" cy="4" r="3"/><circle cx="60" cy="28" r="3"/>
      <circle cx="46" cy="52" r="3"/><circle cx="18" cy="52" r="3"/><circle cx="4" cy="28" r="3"/>
    </g>
    <circle cx="35" cy="31" r="3.5" fill="#1b2d5e"/>
    <g fill="none" stroke="#1b2d5e" stroke-width="2.5" stroke-linecap="round">
      <path d="M28 26 A9 9 0 0 1 40 38"/><path d="M24 20 A16 16 0 0 1 46 40"/>
    </g>
  </svg>
  <p class="reason-text" style="left:593px; width:210px">The increase of IoT (Internet of things)<br>and BYOD (Bring Your Own Device)</p>
</section>

<footer class="footer">Quorvane</footer>

</body>
</html>
```